Business card for STEADYWAVE

Please design professional business card for IT consulting firm STEADYWAVE INC.
Use logo attached.
Use information from sample qNode business card attached.
replace qnode inc with STEADYWAVE INC.
as well as qnodeinc.com with steadywave.example

```html
<!DOCTYPE html>
<html lang="en">
<head>
<meta charset="utf-8">
<title>STEADYWAVE INC. – Business Card</title>
<link rel="stylesheet" href="https://fonts.googleapis.com/css2?family=Open+Sans:wght@400;600;700&display=swap">
<style>
  :root {
    --backdrop: #e6e7e8;
    --card: #f7f7f7;
    --ink: #111111;
    --muted: #8c8c8c;
    --accent: #7a3fd8;
  }
  * { box-sizing: border-box; margin: 0; padding: 0; }
  html, body { width: 1200px; height: 720px; overflow: hidden; }
  body {
    background: var(--backdrop);
    font-family: "Open Sans", Arial, sans-serif;
    color: var(--ink);
    position: relative;
  }
  .card {
    position: absolute;
    left: 180px;
    top: 120px;
    width: 840px;
    height: 480px;
    background: var(--card);
    overflow: hidden;
    box-shadow: 0 6px 20px rgba(0,0,0,0.10);
  }

  .wordmark {
    position: absolute;
    left: 60px;
    top: 130px;
    display: flex;
    align-items: flex-start;
    gap: 6px;
  }
  .wordmark__name {
    font-size: 60px;
    font-weight: 600;
    letter-spacing: 0.2em;
    line-height: 1;
  }
  .wordmark__mark {
    width: 20px;
    height: 20px;
    background: var(--accent);
    margin-top: -18px;
  }

  .person {
    position: absolute;
    left: 60px;
    top: 268px;
  }
  .person__name {
    font-size: 24px;
    font-weight: 700;
    line-height: 1.2;
  }
  .person__name small { font-size: 14px; font-weight: 700; }
  .person__role {
    font-size: 24px;
    font-weight: 400;
    color: var(--muted);
    line-height: 1.2;
  }

  .contact {
    position: absolute;
    left: 510px;
    top: 250px;
    font-size: 15px;
    line-height: 1.55;
  }
  .contact__list {
    display: grid;
    grid-template-columns: 66px auto;
  }
  .contact__list dt { font-weight: 700; }
  .company {
    margin-top: 22px;
    font-style: normal;
  }
  .company__name { font-weight: 700; font-size: 17px; }
</style>
</head>
<body>

<section class="card" aria-label="Business card">
  <div class="wordmark">
    <span class="wordmark__name">STEADYWAVE</span>
    <span class="wordmark__mark"></span>
  </div>
  <div class="person">
    <p class="person__name">DANIEL ORVELL, <small>P.ENG.</small></p>
    <p class="person__role">GENERAL MANAGER</p>
  </div>
  <div class="contact">
    <dl class="contact__list">
      <dt>phone</dt><dd>555-0140 ext.305</dd>
      <dt>mobile</dt><dd>(555) 010-4471</dd>
      <dt>email</dt><dd>dorvell@steadywave.example</dd>
      <dt>site</dt><dd>www.steadywave.example</dd>
    </dl>
    <address class="company">
      <p class="company__name">STEADYWAVE INC.</p>
      <p>1280 Harbourline Rd., Suite 240</p>
      <p>Fairview, Northmere, A1A 1A1, Eastland</p>
    </address>
  </div>
</section>

</body>
</html>
```